Dr Tasneer's Letterhead

I need a professional neat letterhead incorporating my professional information, university titles and qualifications. I have attached my 3 recent ones which contain all the necessary information that needs to be included. I am happy for the information to be a side bar left or right, or as a header/footer combination.

Hello all

I have now made a 2nd and 3rd prize so please submit

Reason: Now there is a 2nd and 3rd place so I can take 3 designs

Industry/Entity Type

University

```html
<!DOCTYPE html>
<html lang="en">
<head>
<meta charset="utf-8">
<title>Dr. Farhan Tasneer — Letterhead</title>
<link rel="stylesheet" href="https://fonts.googleapis.com/css2?family=Ubuntu:wght@400&family=Arimo:wght@400;700&display=swap">
<style>
  :root {
    --paper: #ffffff;
    --brand-blue: #1f3fb0;
    --bar-dark: #1e3a9e;
    --bar-mid: #3f63c7;
    --bar-light: #7d97da;
    --ink: #111111;
    --ink-soft: #2a2a2a;
    --contact-blue: #2447c2;
    --motif-green: #dcf2c2;
    --motif-green-pale: #f1faea;
    --badge-red: #d8463a;
    --badge-navy: #23357d;
    --badge-gold: #e0b64a;
  }
  * { margin: 0; padding: 0; box-sizing: border-box; }
  html, body { width: 860px; height: 1200px; overflow: hidden; background: var(--paper); }
  .letterhead {
    position: relative;
    width: 860px; height: 1200px;
    background: var(--paper);
    font-family: "Arimo", Arial, sans-serif;
    color: var(--ink);
  }
  .masthead { position: absolute; top: 70px; left: 0; width: 860px; text-align: center; }
  .doctor-name {
    font-family: "Ubuntu", sans-serif;
    font-weight: 400;
    font-size: 39px;
    line-height: 44px;
    color: var(--brand-blue);
  }
  .name-rule { display: flex; justify-content: center; margin-top: 4px; height: 4px; }
  .name-rule span { display: block; height: 4px; width: 108px; }
  .name-rule .dark { background: var(--bar-dark); }
  .name-rule .mid { background: var(--bar-mid); margin: 0 3px; }
  .name-rule .light { background: var(--bar-light); }
  .credentials { margin-top: 13px; font-size: 12px; line-height: 20.5px; color: var(--ink-soft); }
  .practice-addresses { margin-top: 8px; font-size: 11.6px; line-height: 14.5px; color: var(--contact-blue); font-style: normal; }

  .molecule-motif {
    position: absolute; left: 18px; top: 662px; width: 268px; height: 528px;
    border-top-right-radius: 134px;
    background: linear-gradient(160deg, var(--motif-green-pale) 0%, var(--motif-green) 55%, var(--motif-green-pale) 100%);
    opacity: 0.85;
  }

  .letter-body { position: absolute; top: 500px; left: 100px; width: 668px; }
  .letter-heading { font-size: 12.6px; font-weight: 700; line-height: 16px; }
  .letter-text { margin-top: 31px; font-size: 12.4px; line-height: 17.2px; color: var(--ink); }

  .footer { position: absolute; top: 1080px; left: 0; width: 860px; text-align: center; }
  .affiliations { display: flex; justify-content: center; align-items: center; gap: 4px; height: 38px; }
  .badge { width: 28px; height: 32px; border-radius: 3px; }
  .badge.red { background: var(--badge-red); }
  .badge.navy { background: var(--badge-navy); }
  .badge.gold { background: var(--badge-gold); width: 16px; }
  .college-name {
    font-family: "Arimo", Arial, sans-serif; font-weight: 400;
    font-size: 18px; color: var(--contact-blue); margin-left: 6px;
  }
  .footer-details { margin-top: 14px; font-size: 11.6px; line-height: 17.5px; color: var(--contact-blue); }
</style>
</head>
<body>
<main class="letterhead">
  <header class="masthead">
    <h1 class="doctor-name">Dr. Farhan Tasneer</h1>
    <div class="name-rule"><span class="dark"></span><span class="mid"></span><span class="light"></span></div>
    <div class="credentials">
      <p>BSc Med, MBBS (Hons 1) NBU, MSc, FCSS (Oto-HNS) • Consultant ENT/Head and Neck Surgeon</p>
      <p>Harbourview Cancer Centre Kellerton Hospital and Kellerton Health District (KHD)</p>
      <p>Senior Lecturer, University of Eastvale (UEV) &amp; Kellerton University (KU)</p>
    </div>
    <address class="practice-addresses">
      <p>Suite 210/48 Linden Road, Kellerton 2150</p>
      <p>7 Marlowe Highway, Ashgrove 2161</p>
      <p>19 Carrow Street, Millbrook 2763</p>
    </address>
  </header>

  <div class="molecule-motif" role="img" aria-label="Pale green molecular network decoration along the lower left margin"></div>

  <section class="letter-body">
    <h2 class="letter-heading">Section 1.10.32 of "de Finibus Bonorum et Malorum", written by Cicero in 45 BC</h2>
    <p class="letter-text">"Sed ut perspiciatis unde omnis iste natus error sit voluptatem accusantium doloremque laudantium, totam rem aperiam, eaque ipsa quae ab illo inventore veritatis et quasi architecto beatae vitae dicta sunt explicabo. Nemo enim ipsam voluptatem quia voluptas sit aspernatur aut odit aut fugit, sed quia consequuntur magni dolores eos qui ratione voluptatem sequi nesciunt. Neque porro quisquam est, qui dolorem ipsum quia dolor sit amet, consectetur, adipisci velit, sed quia non numquam eius modi tempora incidunt ut labore et dolore magnam aliquam quaerat voluptatem. Ut enim ad minima veniam, quis nostrum exercitationem ullam corporis suscipit laboriosam, nisi ut aliquid ex ea commodi consequatur? Quis autem vel eum iure reprehenderit qui in ea voluptate velit esse quam nihil molestiae consequatur, vel illum qui dolorem eum fugiat quo voluptas nulla pariatur?"</p>
  </section>

  <footer class="footer">
    <div class="affiliations">
      <span class="badge red"></span>
      <span class="badge navy"></span>
      <span class="badge gold"></span>
      <span class="college-name">FCSS</span>
    </div>
    <div class="footer-details">
      <p>Provider 5210384K, 318207LP, 318207MQ</p>
      <p>Tel: 95550142 / 95550287 • Fax: 95550391</p>
    </div>
  </footer>
</main>
</body>
</html>
```